IT consultancy business needs logo and business card designed

I need designed business card. it needs to have some wow effect, but simple, corporate and business focused. We provide corporate grade IT services to medium size businesses. These services are IT support over phone, email, in person, VOIP services, IT security , networking - everything that helps business be productivy.

Out tag line will be something along these lines" promoting business growth through use of technology:.

I need a logo designed as well. I am happy to use any colors/theme, perhaps neutral colours, earthy?

Priority: NICE looking, wow design, nice fonts, colors etc... nice logo, business focused but HAS to be modern, wow effect. I will accept anything that looks really cool.

Target Market(s)

Target market are businesses with 20-100 employees. Audience are business decision makers, like general managers, CEO, directors, those are the one seeing this business card;

Industry/Entity Type

Business

Contact Information for Business Card

I am totally flexible, suprise me me something creative:

Dorian Velmek logo on this side(you will design)
managing director ------------------------------- this is line
slogan: technology.delivered.simple

Level 3, 48 Pemberwick Street, Sydney, NSW 2000
dorian@tovrani.com.au
www.tovrani.com.au

back page: logo and slogan: promoting business growth through use of technolog

Requirements
Must have
• Must look modern, cool., wow effect, yet simple and professional.

```html
<!DOCTYPE html>
<html lang="en">
<head>
<meta charset="utf-8">
<title>Tovrani – Business Card</title>
<link href="https://fonts.googleapis.com/css2?family=Open+Sans:wght@400;600;700&display=swap" rel="stylesheet">
<style>
  :root {
    --page-bg: #e6e8ec;
    --card-bg: #ffffff;
    --brand-blue: #2f5f9e;
    --corner-blue-start: #2a5590;
    --corner-blue-end: #5b8fcb;
    --name-navy: #2b3990;
    --text-grey: #3f4349;
    --icon-blue: #3a4fa0;
  }
  * { margin: 0; padding: 0; box-sizing: border-box; }
  html, body {
    width: 1200px; height: 900px; overflow: hidden;
    background: var(--page-bg);
    font-family: "Open Sans", Arial, sans-serif;
  }
  .canvas {
    width: 1200px; height: 900px;
    display: flex; flex-direction: column; align-items: center; justify-content: center;
    gap: 36px;
  }
  .card {
    position: relative;
    width: 700px; height: 400px;
    background: var(--card-bg);
    border-radius: 34px;
    overflow: hidden;
    box-shadow: 0 6px 18px rgba(30, 40, 60, 0.18);
  }
  .card__corner { position: absolute; inset: 0; width: 100%; height: 100%; }

  .brand { position: absolute; display: flex; align-items: center; gap: 16px; }
  .brand__mark {
    width: 62px; height: 62px; border-radius: 50%;
    background: var(--brand-blue);
    flex: none;
  }
  .brand__text { display: flex; flex-direction: column; }
  .brand__name {
    font-weight: 700; font-size: 44px; letter-spacing: 4px; line-height: 1;
    color: var(--brand-blue);
  }
  .brand__tagline {
    font-weight: 400; font-size: 16px; color: var(--text-grey);
    margin-top: 6px; letter-spacing: 0.3px;
  }

  .card--front .brand { left: 36px; top: 50px; }

  .holder { position: absolute; right: 48px; top: 34px; text-align: right; }
  .holder__name {
    font-weight: 700; font-size: 22px; color: var(--name-navy);
    text-transform: uppercase; letter-spacing: 0.3px;
  }
  .holder__role { font-size: 17px; color: var(--text-grey); margin-top: 1px; }

  .contact { position: absolute; left: 40px; bottom: 42px; list-style: none; }
  .contact__item {
    display: flex; align-items: center; gap: 10px;
    font-size: 14px; color: var(--text-grey); line-height: 27px;
  }
  .contact__icon { width: 14px; height: 14px; flex: none; fill: var(--icon-blue); }

  .card--back .brand { left: 50%; top: 150px; transform: translateX(-50%); }
</style>
</head>
<body>
<main class="canvas">

  <section class="card card--front" aria-label="Business card front">
    <svg class="card__corner" viewBox="0 0 700 400" aria-hidden="true">
      <defs>
        <linearGradient id="frontCorner" x1="0" y1="1" x2="1" y2="0">
          <stop offset="0" stop-color="#2a5590"/>
          <stop offset="1" stop-color="#5b8fcb"/>
        </linearGradient>
      </defs>
      <path d="M 470 400 A 230 260 0 0 1 700 140 L 700 400 Z" fill="url(#frontCorner)"/>
    </svg>

    <div class="brand">
      <span class="brand__mark" aria-hidden="true"></span>
      <div class="brand__text">
        <span class="brand__name">TOVRANI</span>
        <span class="brand__tagline">Business Growth Through Technology</span>
      </div>
    </div>

    <div class="holder">
      <p class="holder__name">Dorian Velmek</p>
      <p class="holder__role">Managing Director</p>
    </div>

    <ul class="contact">
      <li class="contact__item">
        <svg class="contact__icon" viewBox="0 0 14 14" aria-hidden="true"><rect x="3.5" y="0.5" width="7" height="13" rx="1.5" fill="none" stroke="#3a4fa0" stroke-width="1.4"/><circle cx="7" cy="11" r="0.9"/></svg>
        020 5550 1478
      </li>
      <li class="contact__item">
        <svg class="contact__icon" viewBox="0 0 14 14" aria-hidden="true"><path d="M3 1 L5.5 3.5 L4.3 5.3 C5 7 6.8 8.8 8.6 9.6 L10.4 8.4 L13 11 L11.4 12.8 C6.5 12.6 1.4 7.5 1.2 2.6 Z"/></svg>
        020 5550 1478
      </li>
      <li class="contact__item">
        <svg class="contact__icon" viewBox="0 0 14 14" aria-hidden="true"><rect x="0.5" y="2.5" width="13" height="9" rx="1"/><path d="M1 3 L7 8 L13 3" fill="none" stroke="#fff" stroke-width="1.2"/></svg>
        dorian@tovrani.com.au
      </li>
      <li class="contact__item">
        <svg class="contact__icon" viewBox="0 0 14 14" aria-hidden="true"><g fill="none" stroke="#3a4fa0" stroke-width="1.2"><circle cx="7" cy="7" r="6"/><ellipse cx="7" cy="7" rx="2.6" ry="6"/><path d="M1 7 H13 M2 4 H12 M2 10 H12"/></g></svg>
        www.tovrani.com.au
      </li>
      <li class="contact__item">
        <svg class="contact__icon" viewBox="0 0 14 14" aria-hidden="true"><path d="M7 0.5 C4.3 0.5 2.4 2.5 2.4 5 C2.4 8.4 7 13.5 7 13.5 C7 13.5 11.6 8.4 11.6 5 C11.6 2.5 9.7 0.5 7 0.5 Z M7 3.3 A1.7 1.7 0 1 1 7 6.7 A1.7 1.7 0 1 1 7 3.3 Z"/></svg>
        Level 3, 48 Pemberwick Street, Sydney, NSW 2000
      </li>
    </ul>
  </section>

  <section class="card card--back" aria-label="Business card back">
    <svg class="card__corner" viewBox="0 0 700 400" aria-hidden="true">
      <defs>
        <linearGradient id="backCorner" x1="0" y1="1" x2="1" y2="0">
          <stop offset="0" stop-color="#2a5590"/>
          <stop offset="1" stop-color="#5b8fcb"/>
        </linearGradient>
      </defs>
      <path d="M 520 400 A 180 210 0 0 1 700 190 L 700 400 Z" fill="url(#backCorner)"/>
    </svg>

    <div class="brand">
      <span class="brand__mark" aria-hidden="true"></span>
      <div class="brand__text">
        <span class="brand__name">TOVRANI</span>
        <span class="brand__tagline">Business Growth Through Technology</span>
      </div>
    </div>
  </section>

</main>
</body>
</html>
```